Wine label design

Need a logo/design for new wine label.
All we have is a label name which is "Marvonetta"
The vineyard is located on rocky hills but we dont really have any design concept in mind. We would like a fun but modern label.

Target Market(s)

Wine consumers. Not too serious. Premium quality product but should be fun and easy to recognise.

Industry/Entity Type

Vineyard

Colors

Designer to choose colors to be used in the design.

Requirements
Must have
• Simple, standout logo/label name
• Contemporary, modern, funky label
• Flexible on colour scheme. Would like it to stand-out and be recognisable but still needs an element of class that reflects premium quality wine.
Nice to have
• Potentially have a link to rolling hills of exposed rock that we produce from.
Should not have
• Old, traditional style label

```html
<!DOCTYPE html>
<html lang="en">
<head>
<meta charset="utf-8">
<title>Marvonetta – Wine Label</title>
<link rel="stylesheet" href="https://fonts.googleapis.com/css2?family=Cinzel:wght@400;600&family=Libre+Baskerville&display=swap">
<style>
  :root {
    --cream-light: #f4e9cc;
    --cream: #ecdcb2;
    --cream-deep: #e2cd98;
    --wine: #8c1748;
    --wine-soft: #b43a72;
    --hill-dark: #5e1f4a;
    --hill-mid: #8a3468;
    --hill-light: #c25a92;
    --frame-gold: #b59a6c;
    --label-white: #ffffff;
  }
  html, body {
    margin: 0;
    padding: 0;
    width: 1131px;
    height: 1200px;
    overflow: hidden;
    background: #ffffff;
  }
  .label {
    position: relative;
    width: 1131px;
    height: 1200px;
    overflow: hidden;
    background: radial-gradient(ellipse at 40% 35%, var(--cream-light) 0%, var(--cream) 55%, var(--cream-deep) 100%);
    font-family: "Cinzel", "Times New Roman", serif;
    color: var(--wine);
  }
  .label__frame {
    position: absolute;
    left: 38px;
    top: 40px;
    right: 38px;
    bottom: 30px;
    border: 2px solid var(--frame-gold);
    z-index: 3;
    pointer-events: none;
  }
  .brand {
    position: absolute;
    top: 110px;
    left: 0;
    right: 0;
    text-align: center;
  }
  .brand__dot {
    display: block;
    width: 46px;
    height: 46px;
    margin: 0 auto 34px;
    border-radius: 50%;
    background: var(--wine);
  }
  .brand__name {
    font-size: 42px;
    font-weight: 400;
    letter-spacing: 2px;
    margin: 0;
  }
  .glass-art {
    position: absolute;
    left: 465px;
    top: 335px;
    width: 200px;
    height: 320px;
    border-radius: 40% 40% 30% 30% / 20% 20% 10% 10%;
    background: linear-gradient(180deg, var(--wine-soft) 0%, var(--wine) 100%);
  }
  .title {
    position: absolute;
    top: 650px;
    left: 0;
    right: 0;
    text-align: center;
    margin: 0;
    font-size: 86px;
    font-weight: 600;
    letter-spacing: 4px;
  }
  .subtitle {
    position: absolute;
    top: 770px;
    left: 0;
    right: 0;
    text-align: center;
    margin: 0;
    font-family: "Libre Baskerville", "Times New Roman", serif;
    font-size: 38px;
    letter-spacing: 1px;
  }
  .hills-art {
    position: absolute;
    left: 0;
    top: 840px;
    width: 1131px;
    height: 360px;
    z-index: 1;
  }
  .volume {
    position: absolute;
    left: 66px;
    bottom: 55px;
    z-index: 2;
    margin: 0;
    font-family: "Libre Baskerville", "Times New Roman", serif;
    font-size: 40px;
    color: var(--label-white);
  }
</style>
</head>
<body>
  <main class="label">
    <div class="label__frame"></div>

    <header class="brand">
      <span class="brand__dot"></span>
      <p class="brand__name">Marvonetta</p>
    </header>

    <div class="glass-art" role="img" aria-label="Illustration of a wine glass filled with a marbled red texture"></div>

    <h1 class="title">Sample Text</h1>
    <p class="subtitle">Your Text Here, Your Text Here</p>

    <svg class="hills-art" viewBox="0 0 1131 360" role="img" aria-label="Illustration of rolling wooded hills in wine tones">
      <defs>
        <linearGradient id="hill-fill" x1="0" y1="0" x2="0" y2="1">
          <stop offset="0" stop-color="var(--hill-light)"/>
          <stop offset="0.35" stop-color="var(--hill-mid)"/>
          <stop offset="1" stop-color="var(--hill-dark)"/>
        </linearGradient>
      </defs>
      <path d="M0 60 C 150 20, 330 10, 470 40 C 640 80, 820 140, 1131 180 L 1131 360 L 0 360 Z" fill="url(#hill-fill)"/>
    </svg>

    <p class="volume">Alc. 17,5% Vol. 750 ml</p>
  </main>
</body>
</html>
```